Business Card Design

wig manufacturer
I would like something very upscale.highend looking
maybe mat chrome card with shiney chrome
or something like the Quorix business card very clean and simple white with the logo in silver
Target Market(s)
upscale women
Industry/Entity Type
Business
Contact Information for Business Card
OUR LOGO
company name:Marisol Tresses
48E52Street Dennis Holcroft
New York,N.Y 10018
Tel:646-5817730
1800-4369185
email:hairloft@zentrimail.com
website:Marisoltresses.com
Look and feel
Each slider illustrates characteristics of the customer's brand and the style your logo design should communicate.

```html
<!DOCTYPE html>
<html lang="en">
<head>
<meta charset="utf-8">
<title>Marisol Tresses – Business Card</title>
<link rel="stylesheet" href="https://fonts.googleapis.com/css2?family=Open+Sans:wght@400;600;700&display=swap">
<style>
  :root {
    --brand-blue: #2e4a8f;
    --card-white: #ffffff;
    --stage: #e9e6e1;
    --ink: #2b2b33;
  }
  * { box-sizing: border-box; margin: 0; padding: 0; }
  html, body { width: 1200px; height: 894px; overflow: hidden; }
  body {
    background: var(--stage);
    font-family: "Open Sans", Arial, sans-serif;
    position: relative;
  }
  .card {
    position: absolute;
    left: 300px;
    width: 600px;
    height: 343px;
    background: var(--card-white);
    border-radius: 18px;
    overflow: hidden;
    box-shadow: 0 6px 20px rgba(0,0,0,0.12);
  }
  .card--front { top: 74px; }
  .card--back { top: 477px; }

  .brand {
    display: flex;
    align-items: center;
    gap: 10px;
    color: var(--brand-blue);
    font-weight: 600;
  }
  .brand__dot {
    border-radius: 50%;
    background: var(--brand-blue);
    flex: none;
  }
  .card--front .brand {
    position: absolute;
    left: 50%;
    top: 50%;
    transform: translate(-50%, -50%);
    font-size: 34px;
    white-space: nowrap;
  }
  .card--front .brand__dot { width: 44px; height: 44px; }

  .card--back .brand {
    position: absolute;
    left: 330px;
    top: 128px;
    font-size: 24px;
    white-space: nowrap;
  }
  .card--back .brand__dot { width: 30px; height: 30px; }

  .name-tab {
    position: absolute;
    left: 0;
    top: 34px;
    width: 300px;
    height: 74px;
    background: var(--brand-blue);
    border-radius: 0 37px 37px 0;
    color: var(--card-white);
    padding: 14px 0 0 34px;
  }
  .name-tab__name {
    font-weight: 700;
    font-size: 22px;
    letter-spacing: 1px;
    line-height: 1.1;
  }
  .name-tab__title {
    font-size: 12.5px;
    letter-spacing: 1.4px;
    margin-top: 4px;
  }

  .contacts {
    position: absolute;
    left: 34px;
    top: 168px;
    list-style: none;
    color: var(--ink);
    font-size: 14.5px;
    letter-spacing: 0.6px;
    text-transform: uppercase;
  }
  .contacts li {
    display: flex;
    align-items: center;
    gap: 12px;
    height: 22px;
  }
  .contacts__icon { width: 16px; height: 16px; flex: none; }
  .contacts__indent { padding-left: 28px; }

  .bottom-band {
    position: absolute;
    left: 0;
    bottom: 0;
    width: 100%;
    height: 30px;
    background: var(--brand-blue);
  }
</style>
</head>
<body>

<section class="card card--front" aria-label="Card front">
  <div class="brand">
    <span class="brand__dot"></span>
    <span class="brand__name">Marisol Tresses</span>
  </div>
</section>

<section class="card card--back" aria-label="Card back">
  <div class="name-tab">
    <p class="name-tab__name">EVAN CARTER</p>
    <p class="name-tab__title">GENERAL MANAGER</p>
  </div>

  <div class="brand">
    <span class="brand__dot"></span>
    <span class="brand__name">Marisol Tresses</span>
  </div>

  <ul class="contacts">
    <li>
      <svg class="contacts__icon" viewBox="0 0 16 16"><circle cx="8" cy="8" r="7.2" fill="none" stroke="#2e4a8f" stroke-width="1.2"/><rect x="5.5" y="4" width="5" height="8" rx="1" fill="none" stroke="#2e4a8f" stroke-width="1.2"/></svg>
      <span>(021) 555 0142</span>
    </li>
    <li>
      <svg class="contacts__icon" viewBox="0 0 16 16"><circle cx="8" cy="8" r="7.2" fill="none" stroke="#2e4a8f" stroke-width="1.2"/><path d="M5 4.5c0 4 2.5 6.5 6.5 7l0.8-1.6-1.8-1-0.9 0.8C8.4 9.2 7 7.8 6.6 6.6l0.8-0.9-1-1.8z" fill="#2e4a8f"/></svg>
      <span>(021) 555 0187</span>
    </li>
    <li>
      <svg class="contacts__icon" viewBox="0 0 16 16"><circle cx="8" cy="8" r="7.2" fill="none" stroke="#2e4a8f" stroke-width="1.2"/><rect x="4" y="5" width="8" height="6" fill="none" stroke="#2e4a8f" stroke-width="1.1"/><path d="M4 5l4 3.5L12 5" fill="none" stroke="#2e4a8f" stroke-width="1.1"/></svg>
      <span>info@marisoltresses.com</span>
    </li>
    <li>
      <svg class="contacts__icon" viewBox="0 0 16 16"><circle cx="8" cy="8" r="7.2" fill="none" stroke="#2e4a8f" stroke-width="1.2"/><circle cx="8" cy="8" r="4" fill="none" stroke="#2e4a8f" stroke-width="1"/><path d="M4 8h8M8 4v8" stroke="#2e4a8f" stroke-width="1"/></svg>
      <span>www.marisoltresses.com</span>
    </li>
    <li>
      <svg class="contacts__icon" viewBox="0 0 16 16"><circle cx="8" cy="8" r="7.2" fill="none" stroke="#2e4a8f" stroke-width="1.2"/><path d="M8 12.5C6 10 5.2 8.6 5.2 7.2a2.8 2.8 0 0 1 5.6 0c0 1.4-0.8 2.8-2.8 5.3z" fill="#2e4a8f"/><circle cx="8" cy="7.2" r="1" fill="#fff"/></svg>
      <span>1030 Harborview Ave,</span>
    </li>
    <li class="contacts__indent"><span>Lakeport, USA</span></li>
  </ul>

  <div class="bottom-band"></div>
</section>

</body>
</html>
```